Business card and stationary for LOGISTICS company | ||
HAULVEX 514K | ||
Use same font as used in my logo | ||
Corporate Modern Professional Simple |
Oleksa | ||
Air and Sea freight from China to Ukraine | ||
Beijing, Lunmao Plaza C4-517K | ||
beijing@haulvex514k.com | ||
www.haulvex514k.com | ||
skype: mvoloshenko | ||
This business card would be given to the new registered client. After registration client receives his own client-number for air and for sea freight. I would need 2 lines on the back with plane and boat logo in front on it so I can write the clients number | ||

```html
<!DOCTYPE html>
<html lang="en">
<head>
<meta charset="utf-8">
<title>HAULVEX 514K — Business Card</title>
<link href="https://fonts.googleapis.com/css2?family=Exo+2:wght@400;600;800&display=swap" rel="stylesheet">
<style>
  :root{
    --bg:#e9ebee;
    --blue:#2f5fb8;
    --blue-deep:#1e4596;
    --blue-light:#4d7fd6;
    --red:#e0262b;
    --white:#ffffff;
    --paper:#f7f8fa;
  }
  *{margin:0;padding:0;box-sizing:border-box}
  html,body{width:1200px;height:963px;overflow:hidden;background:var(--bg);font-family:"Exo 2",sans-serif}
  .card{position:absolute;left:240px;width:720px;height:411px;border-radius:22px;overflow:hidden;box-shadow:0 10px 28px rgba(20,40,80,.22)}
  .card--front{top:47px;background:var(--paper)}
  .card--back{top:505px;background:radial-gradient(circle at 70% 45%,var(--blue-light),var(--blue) 45%,var(--blue-deep))}
  .front-shape{position:absolute;inset:0}
  .brand{position:absolute;left:36px;top:160px;display:flex;align-items:center;gap:10px}
  .brand__dot{width:24px;height:24px;border-radius:50%;background:var(--red);flex:none}
  .brand__name{font-weight:800;font-size:30px;line-height:32px;color:var(--red);letter-spacing:.5px}
  .person{position:absolute;left:340px;top:84px;color:var(--white)}
  .person__name{font-weight:600;font-size:26px;margin-bottom:30px}
  .contacts{list-style:none;font-size:15px;line-height:32px}
  .contacts li{display:flex;align-items:center;gap:12px}
  .contacts svg{width:18px;height:18px;flex:none}
  .web-line{position:absolute;left:44px;top:38px;color:rgba(255,255,255,.85);font-size:15px;letter-spacing:7px}
  .back-mark{position:absolute;right:50px;top:96px;display:flex;align-items:center;gap:14px;opacity:.18}
  .back-mark__dot{width:54px;height:54px;border-radius:50%;background:var(--white)}
  .back-mark__name{font-weight:800;font-size:44px;color:var(--white)}
  .client-lines{position:absolute;left:44px;top:232px;list-style:none}
  .client-line{display:flex;align-items:flex-end;gap:16px;height:40px;margin-bottom:30px}
  .client-line svg{width:34px;height:34px;flex:none}
  .client-line__label{font-size:14px;font-weight:600;color:var(--white);letter-spacing:1px;width:74px;padding-bottom:4px}
  .client-line__rule{width:330px;border-bottom:2px solid rgba(255,255,255,.8);height:1px;margin-bottom:6px}
</style>
</head>
<body>
  <section class="card card--front">
    <svg class="front-shape" viewBox="0 0 720 411" preserveAspectRatio="none">
      <path d="M300 0 C250 120 250 290 300 411 L720 411 L720 0 Z" fill="var(--blue)"/>
      <path d="M282 0 C232 120 232 290 282 411" fill="none" stroke="var(--red)" stroke-width="9"/>
    </svg>
    <div class="brand">
      <span class="brand__dot"></span>
      <span class="brand__name">HAULVEX<br>514K</span>
    </div>
    <div class="person">
      <p class="person__name">Oleksa</p>
      <ul class="contacts">
        <li><svg viewBox="0 0 20 20"><circle cx="10" cy="10" r="10" fill="#fff"/><path d="M10 4a4 4 0 0 0-4 4c0 3 4 8 4 8s4-5 4-8a4 4 0 0 0-4-4z" fill="var(--blue)"/></svg>Beijing, Lunmao Plaza C4-517K</li>
        <li><svg viewBox="0 0 20 20"><circle cx="10" cy="10" r="10" fill="#fff"/><path d="M6 5l2 0 1 3-1.5 1a7 7 0 0 0 3.5 3.5l1-1.5 3 1v2a1 1 0 0 1-1 1A9 9 0 0 1 5 6a1 1 0 0 1 1-1z" fill="var(--blue)"/></svg>+86-10-5550-1472</li>
        <li><svg viewBox="0 0 20 20"><circle cx="10" cy="10" r="10" fill="#fff"/><rect x="7" y="4" width="6" height="12" rx="1.2" fill="var(--blue)"/></svg>+86-139-5550-2831</li>
        <li><svg viewBox="0 0 20 20"><circle cx="10" cy="10" r="10" fill="#fff"/><rect x="5" y="6.5" width="10" height="7" fill="var(--blue)"/><path d="M5 6.5l5 4 5-4" stroke="#fff" fill="none"/></svg>beijing@haulvex514k.com</li>
        <li><svg viewBox="0 0 20 20"><circle cx="10" cy="10" r="10" fill="#fff"/><circle cx="10" cy="10" r="5" fill="none" stroke="var(--blue)" stroke-width="1.4"/><path d="M5 10h10M10 5c-2.5 3-2.5 7 0 10M10 5c2.5 3 2.5 7 0 10" stroke="var(--blue)" fill="none"/></svg>www.haulvex514k.com</li>
      </ul>
    </div>
  </section>

  <section class="card card--back">
    <p class="web-line">www.haulvex514k.com</p>
    <div class="back-mark">
      <span class="back-mark__dot"></span>
      <span class="back-mark__name">HAULVEX 514K</span>
    </div>
    <ul class="client-lines">
      <li class="client-line">
        <svg viewBox="0 0 24 24" aria-label="Air freight"><path d="M21 15v-2l-8-5V3.5a1.5 1.5 0 0 0-3 0V8l-8 5v2l8-2.5V18l-2 1.5V21l3.5-1 3.5 1v-1.5L13 18v-5.5z" fill="#fff"/></svg>
        <span class="client-line__label">AIR No.</span>
        <span class="client-line__rule"></span>
      </li>
      <li class="client-line">
        <svg viewBox="0 0 24 24" aria-label="Sea freight"><path d="M3 14h18l-3 5H6z M6 13V9h5V5h2v4h5v4z" fill="#fff"/><path d="M2 21c2 0 2-1 4-1s2 1 4 1 2-1 4-1 2 1 4 1 2-1 4-1" stroke="#fff" stroke-width="1.3" fill="none"/></svg>
        <span class="client-line__label">SEA No.</span>
        <span class="client-line__rule"></span>
      </li>
    </ul>
  </section>
</body>
</html>
```